Flyer für einen Sanitär Heizungs Betrieb
Zielgruppe
Sanitär Heizungs Betrieb der den Fokus verstärkt auf den Service an Heizungsanlagen setzten will.
Der Flyer soll sowohl an Privathaushalte als auch an Hausverwaltungen gehen.
Er soll unsere Leistungen aufzeigen und einen guten ersten Eindruck vermitteln.
Aufgabenstellung
Anbei sende ich Themen die als Leistung aufgeführt werden, sowie Strichwort für einen Werbetext (kann gerne generiert werden ansonsten kommt er noch zum texter)

```html
<!DOCTYPE html>
<html lang="de">
<head>
<meta charset="utf-8">
<title>Flyer – Energiesparen leicht gemacht</title>
<link href="https://fonts.googleapis.com/css2?family=Open+Sans:wght@400;600;700&display=swap" rel="stylesheet">
<style>
  :root {
    --stage: #b4b4b2;
    --paper: #f7f7f7;
    --ink: #222222;
    --accent-blue: #2e86c8;
    --accent-red: #e0353d;
    --photo-light: #dfe8ee;
    --photo-mid: #9bbad3;
    --photo-warm: #d7b59a;
    --white: #ffffff;
  }
  html, body {
    margin: 0;
    width: 1200px;
    height: 768px;
    overflow: hidden;
    background: var(--stage);
    font-family: "Open Sans", Arial, sans-serif;
  }
  .flyer-cover {
    position: absolute;
    left: 80px;
    top: 134px;
    width: 1040px;
    height: 500px;
    background: var(--paper);
    overflow: hidden;
    box-shadow: 0 10px 30px rgba(0,0,0,0.18);
  }
  .cover-photo {
    position: absolute;
    left: 0;
    top: 0;
    width: 760px;
    height: 100%;
    background:
      radial-gradient(ellipse 260px 220px at 300px 330px, var(--photo-warm) 0%, rgba(215,181,154,0) 70%),
      radial-gradient(ellipse 380px 240px at 300px 420px, var(--photo-mid) 0%, rgba(155,186,211,0) 75%),
      linear-gradient(180deg, var(--photo-light) 0%, #c9d9c4 55%, var(--photo-mid) 100%);
  }
  .cover-photo::after {
    content: "";
    position: absolute;
    inset: 0;
    background: linear-gradient(90deg, rgba(247,247,247,0) 45%, var(--paper) 100%);
  }
  .brand {
    position: absolute;
    right: 56px;
    top: 40px;
    display: flex;
    align-items: center;
    gap: 12px;
  }
  .brand-mark {
    width: 22px;
    height: 22px;
    background: var(--accent-red);
  }
  .brand-name {
    font-size: 24px;
    font-weight: 700;
    color: var(--ink);
  }
  .headline {
    position: absolute;
    right: 56px;
    top: 196px;
    margin: 0;
    text-align: left;
    font-size: 62px;
    font-weight: 400;
    line-height: 1.02;
    letter-spacing: 1px;
    color: var(--ink);
  }
  .subline {
    position: absolute;
    right: 56px;
    top: 338px;
    margin: 0;
    font-size: 25px;
    font-weight: 700;
    color: var(--accent-blue);
  }
  .audience {
    position: absolute;
    left: 150px;
    bottom: 40px;
  }
  .audience-kicker {
    margin: 0 0 6px 28px;
    font-size: 20px;
    font-weight: 700;
    letter-spacing: 1px;
    color: var(--white);
  }
  .audience-band {
    margin: 0;
    padding: 14px 28px;
    background: var(--accent-red);
    color: var(--white);
    font-size: 24px;
    font-weight: 600;
    line-height: 1.25;
    letter-spacing: 1px;
  }
</style>
</head>
<body>
  <article class="flyer-cover">
    <div class="cover-photo" role="img" aria-label="Foto: lächelndes Paar in hellblauen Hemden in einer hellen Wohnung, im Hintergrund Grünpflanzen und Häuser"></div>

    <div class="brand">
      <span class="brand-mark"></span>
      <span class="brand-name">Brennvoll Wärmetechnik GmbH</span>
    </div>

    <h1 class="headline">Energiesparen<br>leicht gemacht!</h1>
    <p class="subline">Heizungssanierung, die zu Ihnen passt!</p>

    <div class="audience">
      <p class="audience-kicker">IHR PARTNER</p>
      <p class="audience-band">FÜR PRIVATHAUSHALTE<br>UND HAUSVERWALTUNGEN</p>
    </div>
  </article>
</body>
</html>
```